Business Card Design Project

My family and I are starting a small business. We need a business card designed for our Australian beef Exporting company. The business card needs to match the logo. The project I've launched is called "Logo design for an Australian beef export company specifically for the China market (Contest)"

Target Market(s)

Our customer
- Chinese businessmen
- In the hospitality industry
- They value Australian produce (e.g. wine and beef)

When a consumer sees it I want them to see:
- Quality
- Tradition
- Strength, Trust and partnership
- Australian made-rustic
- Chinese business culture relevance
- Family

The above elements are important to our Chinese customer. I also want the logo to look clean and professional.

The product we're selling is:
- Exporting Australian Beef to China
- We may in the future export other meats and products too.
- Clean and green Beef

Chinese cultural relevance
- The logo must be relevant to Chinese business culture

Industry/Entity Type

Business

Font styles to use
Sans Serif

Colors
0355a3
ec1f27

Requirements
Must have
• SIDE ONE
- Include the logo: it's currently being designed by ArtHive
- Elements of the business card
Phone
Email
Mobile
Web www.tallowridgemeats.asia
Favourite Cut
Full name
Role
Text (Office locations): SYDNEY KELBARRA

Colours
- Red: similar tone in the Chinese flag
- Gold: use gold to line the logo
- Blue

SIDE 2
- Image attached of the sunrise
- add text: Kelbarra Station, Queensland, Australia

```html
<!DOCTYPE html>
<html lang="en">
<head>
<meta charset="utf-8">
<title>Tallowridge Meats – Business Card</title>
<link href="https://fonts.googleapis.com/css2?family=Open+Sans:wght@400;600;700&display=swap" rel="stylesheet">
<style>
  :root {
    --brand-blue: #0355a3;
    --brand-blue-deep: #0a3f7a;
    --brand-red: #ec1f27;
    --gold: #e7c53a;
    --paper: #ffffff;
    --ink-grey: #6c7a8a;
    --map-grey: #e4e6ea;
    --backdrop: #e9e6e1;
    --white: #ffffff;
  }
  * { box-sizing: border-box; margin: 0; padding: 0; }
  html, body { width: 1200px; height: 1023px; overflow: hidden; }
  body {
    background: var(--backdrop);
    font-family: "Open Sans", Arial, sans-serif;
    position: relative;
  }
  .card {
    position: absolute;
    left: 250px;
    width: 700px;
    height: 400px;
    border-radius: 4px;
    overflow: hidden;
    box-shadow: 0 8px 24px rgba(0,0,0,0.18);
  }
  .card--front { top: 62px; background: var(--paper); }
  .card--back { top: 560px; }

  .front-map {
    position: absolute;
    left: 360px; top: 18px;
    width: 210px; height: 160px;
    border-radius: 40% 55% 45% 50%;
    background: var(--map-grey);
    opacity: 0.8;
  }
  .front-wave { position: absolute; inset: 0; }

  .brand-mark {
    position: absolute;
    left: 40px; top: 52px;
    display: flex; align-items: center; gap: 14px;
  }
  .brand-mark__dot {
    width: 46px; height: 46px; border-radius: 50%;
    background: var(--brand-blue);
    border: 3px solid var(--gold);
  }
  .brand-mark__name {
    font-size: 26px; font-weight: 700; color: var(--brand-blue);
  }

  .person {
    position: absolute;
    left: 40px; top: 168px;
    display: flex; align-items: baseline; gap: 10px;
    color: var(--brand-blue);
  }
  .person__name { font-size: 30px; font-weight: 600; }
  .person__role {
    font-size: 17px; color: var(--ink-grey);
    border-left: 2px solid var(--ink-grey); padding-left: 10px;
  }

  .contact {
    position: absolute;
    list-style: none;
    color: var(--white);
    font-size: 16px;
    white-space: nowrap;
  }
  .contact li { display: flex; align-items: center; gap: 10px; margin-bottom: 8px; }
  .contact__icon {
    width: 16px; height: 16px; border-radius: 50%;
    background: var(--gold); flex: none;
  }
  .contact--phones { left: 40px; top: 300px; }
  .contact--office { left: 235px; top: 300px; text-transform: uppercase; }
  .contact--online { left: 450px; top: 300px; }

  .back-photo {
    position: absolute; inset: 0;
    background:
      radial-gradient(ellipse at 28% 32%, rgba(255,236,150,0.95) 0%, rgba(230,180,80,0.6) 18%, rgba(0,0,0,0) 45%),
      linear-gradient(180deg, #8c8470 0%, #6d6a72 38%, #3e3c48 60%, #24232b 100%);
  }
  .back-caption {
    position: absolute;
    left: 0; right: 0; top: 176px;
    text-align: center;
    color: var(--white);
    font-size: 30px; font-weight: 400;
    letter-spacing: 0.5px;
  }
</style>
</head>
<body>

<section class="card card--front" aria-label="Business card front">
  <div class="front-map" role="img" aria-label="Faint dotted map of Australia"></div>
  <svg class="front-wave" viewBox="0 0 700 400" aria-hidden="true">
    <path d="M0 275 C170 262 300 250 420 170 C520 100 610 28 700 0 L700 400 L0 400 Z" fill="var(--brand-blue)"/>
    <path d="M420 170 C520 100 610 28 700 0 L700 14 C612 42 526 112 432 176 Z" fill="var(--brand-red)"/>
    <path d="M0 285 C180 272 310 258 432 180 C530 116 616 48 700 22" fill="none" stroke="var(--brand-red)" stroke-width="1.2"/>
    <line x1="0" y1="376" x2="700" y2="376" stroke="var(--brand-red)" stroke-width="1"/>
  </svg>

  <div class="brand-mark">
    <span class="brand-mark__dot"></span>
    <span class="brand-mark__name">Tallowridge Meats</span>
  </div>

  <div class="person">
    <span class="person__name">Liam Carter</span>
    <span class="person__role">Director</span>
  </div>

  <ul class="contact contact--phones">
    <li><span class="contact__icon"></span>07 5550 0144</li>
    <li><span class="contact__icon"></span>07 5550 0177</li>
  </ul>
  <ul class="contact contact--office">
    <li><span class="contact__icon"></span>Sydney Kelbarra</li>
  </ul>
  <ul class="contact contact--online">
    <li><span class="contact__icon"></span>info@tallowridgemeats.asia</li>
    <li><span class="contact__icon"></span>www.tallowridgemeats.asia</li>
  </ul>
</section>

<section class="card card--back" aria-label="Business card back">
  <div class="back-photo" role="img" aria-label="Sunrise over hills and water at Kelbarra Station"></div>
  <p class="back-caption">Kelbarra Station, Queensland, Australia</p>
</section>

</body>
</html>
```